Tarrow Cat Hotel needs a website and a logo :)

I need a web design for my pet hotel. I will use it in Wordpress, probable with Elementor, so if you can also offer the WP template creation, that's a bonus but I don't wanna book the coded-website option here as I don't think that applies to WP. It would be great if you come up with a logo as well.

Here some info:

Modern, premium cat boarding with a vet on-site

Tarrow Cat Hotel is a boutique cat boarding facility in Nelson, New Zealand, offering high-quality, vet-supervised care for all cats, including those with special medical needs. Unlike standard catteries, we focus on low-stress boarding, with separate spaces for special-needs and healthy cats, ensuring a safe, comfortable, and peaceful environment. We also prioritize convenience with self check-in and check-out, leveraging technology to enhance the experience.

Target Market(s)

Cat owners for short term to long term stays that don't want the cheapest option and will value that we have a vet on-site

Industry/Entity Type

cat boarding

Number of Pages Required

5+ page

Font styles to use
Sans Serif
Other font styles liked:
• Nothing that needs installation or a license. Please use Google Fonts.

Requirements
Must have
• Landing page, about us, services, blog and contact page - the landing page should have the typical sales layout with hero image top right, a tag line "Modern, premium cat boarding with a vet on-site" and 2 paragraphs. Paragraph 1 (Problem): Leaving your cat behind can be stressful, especially if they need special care. Standard catteries often lack vet oversight and a calm, tailored environment. Paragraph 2 (Solution): At Tarrow Cat Hotel, we offer premium, vet-supervised boarding with separate spaces for special-needs and healthy cats. Our self check-in and tech-driven system makes drop-offs and pick-ups effortless... you know the drill :)
Nice to have
• Ask ChatGPT for some ideas and give it the business plan: https://files.brimlodge.example/doc/8qTxR2vLmPz4KwYc7NbHs3JfDgUeVa1oZiQy/view?share=open
Should not have
• NO DOGS :)

```html
<!DOCTYPE html>
<html lang="en">
<head>
<meta charset="utf-8">
<title>Purrwell — Premium Cat Boarding</title>
<link href="https://fonts.googleapis.com/css2?family=Poppins:wght@400;500;600;700;800&display=swap" rel="stylesheet">
<style>
:root{
  --orange:#f47b20;
  --ink:#111111;
  --text:#444444;
  --muted:#666666;
  --white:#ffffff;
  --black:#000000;
  --footer:#231f20;
  --stage:#9b9b9b;
  --line:#3a3a3a;
}
*{margin:0;padding:0;box-sizing:border-box}
html,body{width:1200px;height:2559px;overflow:hidden;background:var(--stage);font-family:'Poppins',sans-serif}
.page{position:absolute;left:110px;top:92px;width:988px;height:2391px;background:var(--white);overflow:hidden}
.abs{position:absolute}
.btn{position:absolute;display:flex;align-items:center;justify-content:center;background:var(--orange);color:var(--white);font-size:8.5px;font-weight:600;text-transform:uppercase;letter-spacing:.2px}
/* hero */
.hero{position:absolute;left:0;top:0;width:988px;height:446px;background:linear-gradient(90deg,#2d2d2d 0%,#4a4a4a 35%,#cfcfcc 60%,#e6e3de 78%,#b8c4d6 100%)}
.hero-shade{position:absolute;inset:0;background:linear-gradient(90deg,rgba(0,0,0,.55) 0%,rgba(0,0,0,.35) 45%,rgba(0,0,0,0) 70%)}
.brand{position:absolute;left:160px;top:20px;display:flex;align-items:center;gap:6px;color:var(--orange);font-size:15px;font-weight:500}
.brand-dot{width:16px;height:16px;border-radius:50%;background:var(--orange)}
.nav{position:absolute;left:443px;top:21px;display:flex;gap:20px;font-size:8.5px;color:var(--white)}
.nav .active{color:var(--orange)}
.hero h1{position:absolute;left:160px;top:184px;width:380px;color:var(--white);font-size:23px;line-height:31px;font-weight:700}
.hero p{position:absolute;left:160px;top:259px;width:290px;color:#eee;font-size:8.5px;line-height:16px}
.btn-outline{position:absolute;left:279px;top:305px;width:86px;height:31px;border:1.5px solid var(--white);color:var(--white);font-size:8.5px;font-weight:500;display:flex;align-items:center;justify-content:center}
.counter{position:absolute;left:763px;top:382px;color:var(--white);font-size:27px;font-weight:700}
.counter small{font-size:16px}
/* intro */
.section-title{position:absolute;width:988px;text-align:center;color:var(--ink);font-weight:700}
.subtitle{position:absolute;top:515px;width:988px;text-align:center;font-size:8.5px;color:var(--text)}
.timeline{position:absolute;left:163px;top:636px;width:661px;border-top:1px dashed #999}
.tl-dot{position:absolute;top:633px;width:7px;height:7px;border-radius:50%;background:var(--orange)}
.feature{position:absolute;top:552px;width:118px;height:169px;background:var(--white);box-shadow:0 4px 18px rgba(0,0,0,.12)}
.feature svg{position:absolute;left:36px;top:20px}
.feature .knob{position:absolute;left:54px;top:98px;width:10px;height:10px;border:1px dashed #888;border-radius:50%}
.feature .stem{position:absolute;left:58.5px;top:84px;height:14px;border-left:1px dashed #888}
.feature h3{position:absolute;top:125px;width:118px;text-align:center;font-size:10.5px;line-height:13.5px;font-weight:600;color:var(--ink)}
/* why */
.why-photo{position:absolute;left:160px;top:767px;width:316px;height:338px;background:linear-gradient(160deg,#3f7fc1 0%,#d9dde2 35%,#ecedef 60%,#9ea3a8 100%);z-index:2}
.why h2{position:absolute;left:518px;top:829px;font-size:22px;font-weight:700;color:var(--ink)}
.why p{position:absolute;left:518px;top:864px;width:305px;font-size:8.5px;line-height:16px;color:var(--text)}
/* services */
.services{position:absolute;left:0;top:1055px;width:988px;height:348px;background:var(--black)}
.services h2{position:absolute;left:160px;top:90px;color:var(--white);font-size:22px;font-weight:700}
.grid{position:absolute;left:147px;top:137px;width:695px;height:182px}
.cell{position:absolute;width:167px;height:91px;display:flex;align-items:center;gap:14px;padding-left:36px;color:var(--white);font-size:9.5px;font-weight:600;line-height:12px}
.vline{position:absolute;top:0;height:182px;border-left:1px solid var(--line)}
.hline{position:absolute;left:0;top:91px;width:695px;border-top:1px solid var(--line)}
.cell.hot{background:var(--orange);display:block;padding:30px 14px 0 16px}
.cell.hot h4{font-size:9.5px;font-weight:600}
.cell.hot p{font-size:8.3px;font-weight:400;line-height:12px;margin-top:2px}
.hot-badge{position:absolute;left:363px;top:-20px;width:40px;height:40px;background:var(--white);display:flex;align-items:center;justify-content:center}
/* gallery */
.card{position:absolute;top:1508px;width:214px;height:240px}
.card .shade{position:absolute;inset:0;background:linear-gradient(180deg,rgba(0,0,0,0) 55%,rgba(0,0,0,.7) 100%)}
.card .cap{position:absolute;left:18px;top:180px;width:190px;color:var(--white);font-size:8.5px;line-height:14px}
.card .cap b{font-weight:600;display:block}
.card .go{position:absolute;left:172px;top:228px;width:24px;height:24px;background:var(--orange);display:flex;align-items:center;justify-content:center}
.view-all{position:absolute;top:1776px;width:988px;text-align:center;font-size:9px;font-weight:600;color:var(--ink)}
.view-all span{border-bottom:1px solid var(--ink)}
/* testimonials */
.testi-bg{position:absolute;left:0;top:1824px;width:494px;height:314px;background:radial-gradient(ellipse at 55% 35%,#f4f4f4 0%,#e3e3e3 60%,#d8d8d8 100%)}
.testi-photo{position:absolute;left:494px;top:1824px;width:494px;height:314px;background:linear-gradient(120deg,#d7d3da 0%,#f1eff2 45%,#c9c5cc 100%)}
.testi h2{position:absolute;left:160px;top:1882px;font-size:22px;font-weight:700;color:var(--ink)}
.stars{position:absolute;left:160px;top:1918px;display:flex;gap:3px}
.testi p{position:absolute;left:160px;top:1941px;width:285px;font-size:8.5px;line-height:16px;color:var(--text)}
.avatar{position:absolute;left:160px;top:2010px;width:35px;height:35px;border-radius:50%;background:linear-gradient(135deg,#e25b4a,#f0a07a)}
.who{position:absolute;left:208px;top:2017px;font-size:9px;line-height:11px;color:var(--ink)}
.who b{font-weight:600;display:block}
.arrows{position:absolute;left:160px;top:2062px;display:flex;gap:14px}
/* footer */
.footer{position:absolute;left:0;top:2138px;width:988px;height:253px;background:var(--footer);color:var(--white)}
.col{position:absolute;top:60px;font-size:8.5px}
.col h5{font-size:10.5px;font-weight:600;margin-bottom:16px}
.col li{list-style:none;line-height:17.5px}
.col .lab{font-weight:600;margin-top:0}
.col .grp{line-height:10px;margin-bottom:12px}
.news-input{position:absolute;left:649px;top:117px;width:180px;height:34px;background:#3a3637;display:flex;align-items:center;justify-content:space-between;padding:0 10px 0 12px;font-size:8.5px;color:#aaa}
.rule{position:absolute;left:160px;top:217px;width:669px;border-top:1px solid #4a4647}
.copy{position:absolute;top:231px;width:988px;text-align:center;font-size:8.5px}
.to-top{position:absolute;left:838px;top:194px;width:31px;height:31px;background:var(--orange);display:flex;align-items:center;justify-content:center}
</style>
</head>
<body>
<main class="page">

  <header class="hero">
    <div class="abs" style="inset:0" role="img" aria-label="Veterinary nurse opening a cat suite door where a white cat rests on a blue cushion"></div>
    <div class="hero-shade"></div>
    <div class="brand"><span class="brand-dot"></span>Purrwell</div>
    <nav class="nav"><span class="active">Home</span><span>About Us</span><span>Services</span><span>Blog</span><span>Testimonials</span></nav>
    <div class="btn" style="left:727px;top:12px;width:102px;height:32px">Get Started</div>
    <h1>Modern, Premium Cat Boarding with a Vet On-Site</h1>
    <p>Luxury cat accommodation in Nelson, NZ – designed for comfort, health, and peace of mind.</p>
    <div class="btn" style="left:160px;top:305px;width:110px;height:31px">Our Services</div>
    <div class="btn-outline">CONTACT US</div>
    <div class="counter">01/<small>03</small></div>
  </header>

  <h2 class="section-title" style="top:481px;font-size:22px">Purrwell</h2>
  <p class="subtitle">Leaving Your Cat Behind Shouldn't Be Stressful</p>
  <div class="timeline"></div>
  <span class="tl-dot" style="left:160px"></span>
  <span class="tl-dot" style="left:821px"></span>

  <article class="feature" style="left:209px">
    <svg width="46" height="46" viewBox="0 0 46 46" fill="none" stroke="#f47b20" stroke-width="2"><path d="M4 3h28v40H4z"/><path d="M9 10h18M9 16h10M9 22h8"/><path d="M28 20l12 22H16z"/><path d="M28 30v5"/><circle cx="28" cy="38" r="1"/></svg>
    <span class="stem"></span><span class="knob"></span>
    <h3>Problem<br>Paragraph</h3>
  </article>
  <article class="feature" style="left:359px">
    <svg width="46" height="46" viewBox="0 0 46 46" fill="none" stroke="#f47b20" stroke-width="2"><path d="M2 6h16M2 14h12M2 22h16M2 30h12M2 38h16"/><path d="M24 6h18M28 14h14M24 22h18"/><path d="M24 32h16l-5-5M40 32l-5 5"/></svg>
    <span class="stem"></span><span class="knob"></span>
    <h3>Solution<br>Paragraph</h3>
  </article>
  <article class="feature" style="left:510px">
    <svg width="46" height="46" viewBox="0 0 46 46" fill="none" stroke="#f47b20" stroke-width="2"><path d="M3 4h40v30H3z"/><path d="M23 34v8M15 42h16"/><ellipse cx="13" cy="12" rx="6" ry="4"/><path d="M20 28v-8h5v8M28 28V14h5v14M36 28v-6"/></svg>
    <span class="stem"></span><span class="knob"></span>
    <h3 style="top:131px">Visuals</h3>
  </article>
  <article class="feature" style="left:661px">
    <svg width="46" height="46" viewBox="0 0 46 46" fill="none" stroke="#f47b20" stroke-width="2"><path d="M14 4h18l7 8-16 14L7 12z"/><path d="M7 12h32M18 4l5 8 5-8M23 12v14"/><path d="M23 26v14"/><path d="M23 40c-4-8-12-8-16-6 4 6 10 8 16 6zM23 40c4-8 12-8 16-6-4 6-10 8-16 6z"/></svg>
    <span class="stem"></span><span class="knob"></span>
    <h3>Luxury<br>Environment</h3>
  </article>

  <section class="why">
    <div class="why-photo" role="img" aria-label="Staff member holding a cat beside white boarding suites in a bright corridor"></div>
    <h2>Why Choose Us Purrwell?</h2>
    <p>Lorem ipsum dolor sit amet, consectetuer adipiscing elit, sed diam nonummy nibh euismod tincidunt ut laoreet dolore magna aliquam erat volutpat.</p>
    <div class="btn" style="left:518px;top:928px;width:89px;height:31px">Read More</div>
  </section>

  <section class="services">
    <h2>Our Services</h2>
    <div class="btn" style="left:739px;top:88px;width:90px;height:32px">Read More</div>
    <div class="grid">
      <div class="cell" style="left:0;top:0">
        <svg width="36" height="36" viewBox="0 0 36 36" fill="none" stroke="#fff" stroke-width="1.6"><path d="M3 26h30M6 26c0-8 6-13 12-13s12 5 12 13"/><path d="M10 30h16"/><circle cx="18" cy="8" r="3"/><path d="M28 4l2 2M8 4L6 6"/></svg>
        <span>Luxury<br>Environment:</span></div>
      <div class="cell" style="left:180px;top:0">
        <svg width="40" height="36" viewBox="0 0 40 36" fill="none" stroke="#fff" stroke-width="1.6"><path d="M2 3h32v22H2z"/><path d="M18 25v6M11 31h14"/><circle cx="18" cy="15" r="4"/><circle cx="12" cy="9" r="2"/><circle cx="24" cy="9" r="2"/><path d="M33 20a5 5 0 0 1 5 5c0 4-5 9-5 9s-5-5-5-9a5 5 0 0 1 5-5z"/></svg>
        <span>Vet On-Site:</span></div>
      <div class="cell hot" style="left:347px;top:0">
        <div class="hot-badge" style="left:16px;top:-20px">
          <svg width="24" height="22" viewBox="0 0 24 22" fill="none" stroke="#f47b20" stroke-width="1.4"><path d="M3 2h18v13H3zM1 18h22"/><circle cx="12" cy="8" r="3"/><path d="M12 3v2M12 11v2M7 8h2M15 8h2"/></svg>
        </div>
        <h4>Tech-Driven Updates:</h4>
        <p>Lorem ipsum dolor sit amet, consectetuer adipiscing elit, sed diam nonummy.</p>
      </div>
      <div class="cell" style="left:514px;top:0">
        <svg width="34" height="36" viewBox="0 0 34 36" fill="none" stroke="#fff" stroke-width="1.6"><path d="M3 2h22v32H3z"/><path d="M7 8h14M7 13h8"/><path d="M22 15l10 19H12z"/><path d="M22 23v5"/></svg>
        <span>Problem<br>Paragraph:</span></div>

      <div class="cell" style="left:0;top:91px">
        <svg width="36" height="36" viewBox="0 0 36 36" fill="none" stroke="#fff" stroke-width="1.6"><path d="M3 26h30M6 26c0-8 6-13 12-13s12 5 12 13"/><path d="M10 30h16"/><circle cx="18" cy="8" r="3"/><path d="M28 4l2 2M8 4L6 6"/></svg>
        <span>Luxury<br>Environment:</span></div>
      <div class="cell" style="left:180px;top:91px">
        <svg width="40" height="36" viewBox="0 0 40 36" fill="none" stroke="#fff" stroke-width="1.6"><path d="M2 3h32v22H2z"/><path d="M18 25v6M11 31h14"/><circle cx="18" cy="15" r="4"/><circle cx="12" cy="9" r="2"/><circle cx="24" cy="9" r="2"/><path d="M33 20a5 5 0 0 1 5 5c0 4-5 9-5 9s-5-5-5-9a5 5 0 0 1 5-5z"/></svg>
        <span>Vet On-Site:</span></div>
      <div class="cell" style="left:347px;top:91px">
        <svg width="40" height="34" viewBox="0 0 40 34" fill="none" stroke="#fff" stroke-width="1.6"><path d="M6 4h28v20H6zM2 30h36"/><circle cx="20" cy="14" r="5"/><path d="M20 6v3M20 19v3M12 14h3M25 14h3"/></svg>
        <span>Tech-Driven<br>Updates:</span></div>
      <div class="cell" style="left:514px;top:91px">
        <svg width="34" height="36" viewBox="0 0 34 36" fill="none" stroke="#fff" stroke-width="1.6"><path d="M3 2h22v32H3z"/><path d="M7 8h14M7 13h8"/><path d="M22 15l10 19H12z"/><path d="M22 23v5"/></svg>
        <span>Problem<br>Paragraph:</span></div>

      <span class="vline" style="left:180px"></span>
      <span class="vline" style="left:347px"></span>
      <span class="vline" style="left:514px"></span>
      <span class="hline"></span>
    </div>
  </section>

  <h2 class="section-title" style="top:1466px;font-size:22px">Favorite Cats Our Gallery</h2>

  <figure class="card" style="left:160px">
    <div class="abs" style="inset:0;background:linear-gradient(150deg,#e9dccb 0%,#c9a47c 45%,#5b4a3b 100%)" role="img" aria-label="Two long-haired cats nuzzling"></div>
    <div class="shade"></div>
    <figcaption class="cap"><b>Bengal cat:</b>Lorem ipsum dolor sit amet, consectetuer adipiscing elit, erat volutpat.</figcaption>
    <span class="go"><svg width="8" height="10" viewBox="0 0 8 10" fill="none" stroke="#fff" stroke-width="1.8"><path d="M2 1l4 4-4 4"/></svg></span>
  </figure>
  <figure class="card" style="left:387px">
    <div class="abs" style="inset:0;background:linear-gradient(150deg,#5a4636 0%,#c78a4f 45%,#8a5a34 100%)" role="img" aria-label="Ginger cat being brushed by hand"></div>
    <div class="shade"></div>
    <figcaption class="cap"><b>American Shorthair:</b>Lorem ipsum dolor sit amet, consectetuer adipiscing elit, erat volutpat.</figcaption>
    <span class="go"><svg width="8" height="10" viewBox="0 0 8 10" fill="none" stroke="#fff" stroke-width="1.8"><path d="M2 1l4 4-4 4"/></svg></span>
  </figure>
  <figure class="card" style="left:614px">
    <div class="abs" style="inset:0;background:linear-gradient(150deg,#d6d8d6 0%,#a58d70 50%,#6d5a48 100%)" role="img" aria-label="Tabby kitten looking upward"></div>
    <div class="shade"></div>
    <figcaption class="cap"><b>Devon Rex:</b>Lorem ipsum dolor sit amet, consectetuer adipiscing elit, erat volutpat.</figcaption>
    <span class="go"><svg width="8" height="10" viewBox="0 0 8 10" fill="none" stroke="#fff" stroke-width="1.8"><path d="M2 1l4 4-4 4"/></svg></span>
  </figure>

  <p class="view-all"><span>VIEW ALL PROJECT</span></p>

  <section class="testi">
    <div class="testi-bg" role="img" aria-label="Faint white cat backdrop"></div>
    <div class="testi-photo" role="img" aria-label="Row of white boarding suites with a black and white cat inside"></div>
    <h2>Testimonials</h2>
    <div class="stars">
      <svg width="13" height="13" viewBox="0 0 24 24"><path fill="#f6c61b" d="M12 2l3 7h7l-6 4.5 2.3 7.5L12 16.5 5.7 21 8 13.5 2 9h7z"/></svg>
      <svg width="13" height="13" viewBox="0 0 24 24"><path fill="#f6c61b" d="M12 2l3 7h7l-6 4.5 2.3 7.5L12 16.5 5.7 21 8 13.5 2 9h7z"/></svg>
      <svg width="13" height="13" viewBox="0 0 24 24"><path fill="#f6c61b" d="M12 2l3 7h7l-6 4.5 2.3 7.5L12 16.5 5.7 21 8 13.5 2 9h7z"/></svg>
      <svg width="13" height="13" viewBox="0 0 24 24"><path fill="#f6c61b" d="M12 2l3 7h7l-6 4.5 2.3 7.5L12 16.5 5.7 21 8 13.5 2 9h7z"/></svg>
      <svg width="13" height="13" viewBox="0 0 24 24"><path fill="#f6c61b" d="M12 2l3 7h7l-6 4.5 2.3 7.5L12 16.5 5.7 21 8 13.5 2 9h7z"/></svg>
    </div>
    <p>Lorem ipsum dolor sit amet, consectetuer adipiscing elit, sed diam nonummy nibh euismod tincidunt ut laoreet dolore magna aliquam erat volutpat.</p>
    <div class="avatar" role="img" aria-label="Customer portrait"></div>
    <div class="who"><b>Mara T.</b>Project Manger</div>
    <div class="arrows">
      <svg width="12" height="10" viewBox="0 0 12 10" fill="none" stroke="#333" stroke-width="1.2"><path d="M11 5H1M5 1L1 5l4 4"/></svg>
      <svg width="22" height="12" viewBox="0 0 22 12" fill="none" stroke="#f47b20" stroke-width="1.4"><path d="M1 6h20M15 1l6 5-6 5"/></svg>
    </div>
  </section>

  <footer class="footer">
    <div class="col" style="left:160px"><h5>Why Choose Us</h5>
      <ul><li>Home</li><li>About Us</li><li>Services</li><li>Project</li><li>Testimonials</li></ul></div>
    <div class="col" style="left:312px"><h5>Information</h5>
      <ul><li>Privacy Policy</li><li>Disclaimer</li><li>Terms &amp; Candition</li><li>Site Map</li></ul></div>
    <div class="col" style="left:456px"><h5>Contact Us</h5>
      <div class="grp"><div class="lab">PHONE</div>(808)555-0142</div>
      <div class="grp"><div class="lab">EMAIL</div>hello@purrwell.example</div>
      <div class="grp"><div class="lab">ADDRESS</div>212 Kelby Lane Ste 40<br>Harbor City, HI 96899</div></div>
    <div class="col" style="left:649px"><h5>Newsletter</h5><p>Subscribe to our newsletter</p></div>
    <div class="news-input">Enter email address
      <svg width="11" height="11" viewBox="0 0 24 24" fill="#fff"><path d="M22 2L2 10l8 3 3 9z"/></svg></div>
    <span class="to-top"><svg width="8" height="6" viewBox="0 0 8 6" fill="none" stroke="#fff" stroke-width="1.4"><path d="M1 5l3-3 3 3"/></svg></span>
    <div class="rule"></div>
    <p class="copy">Copyright © 2024 Halvern Brokers, LLC All rights reserved | Privacy and cookie policy Terms | Privacy | Cookies</p>
  </footer>

</main>
</body>
</html>
```